Automotive Locksmiith company needs a website design and mobile website

We need a website design and a mobile design for an automotive locksmith company called Halvern Keyworks LLC.We are based in the center of the Dallas-Fort Worth Metroplex. We have a website that was directed more towards the towing services we also offer. We would like to have it more towards our locksmith products. Our main services include:
Auto keys duplication
Cutting of new car keys
Car Lockouts
Laser key replacement
Cutting keys by code
Broken key extractions
Production of transponder keys
Key fob programming
Door lock repairs
Ignition repairs/replacement
We work on 95% of the automotive market that includes Vorla, Tessin, QRT, Pembrook, Marquenne, Dunmoral, Brask, VX, Sorvalo, Kelto, Zephrane, Oru, Hadley, Norax, Tabori, Valdrenne, Quillon, Pipo, Runel Okarawe , Brevik, Solumé, Drennhofer, Kestra.
We are one of the most affordable services in the DFW area . Our prices for transponder copies start at $35 per key. We provide services for high-end vehicles also as QRT and Valdrenne. We can program the new proximity keys for Tabori Vehicles 2013-up. We also work on the new Pell Vehicles 20-13 and up including the Pell Arden head remote key.
We would like to have a similar style to the website we already have with the option to schedule an appointment on the mobile website. This mobile application will deliver an email when a new customer is requiring the service. It will ask for Year, Make, Model , Service to be performed( Key copy, Lockout, Lost Key, Change Ignition lock, change door lock, Other services.) Description of the service to be performed, Address, Select time of service.
Our current website is halvernkeyworks.example

Reason: Need pictures of webpages inside design (about us , location etc) and mobile pictures( how website looks in Quorra / android)

Automotive

• check word attachment

```html
<!DOCTYPE html>
<html lang="en">
<head>
<meta charset="utf-8">
<title>Halvern Keyworks LLC</title>
<link href="https://fonts.googleapis.com/css2?family=Roboto+Condensed:wght@400;700&display=swap" rel="stylesheet">
<style>
:root{
  --backdrop:#383838;
  --page:#ffffff;
  --blue:#1f86c9;
  --navy:#0b3768;
  --cyan:#2aa9e0;
  --card:#f1f1f1;
  --text:#3f3f3f;
  --muted:#9a9a9a;
  --footer:#3c3c3c;
  --icon:#d7d7d7;
}
*{margin:0;padding:0;box-sizing:border-box}
html,body{width:1060px;height:1200px;overflow:hidden}
body{background:var(--backdrop);font-family:"Roboto Condensed",Arial,sans-serif;color:var(--text);position:relative}
.page{position:absolute;left:88px;top:14px;width:883px;height:1186px;background:var(--page)}
.abs{position:absolute}

.brand{left:22px;top:74px;display:flex;align-items:center;gap:8px}
.brand-square{width:16px;height:16px;background:var(--cyan)}
.brand-name{font-size:28px;font-weight:700;color:var(--navy);letter-spacing:-.3px}

.contact{display:flex;align-items:center;gap:8px;font-size:14px;line-height:18px;color:#222}
.contact-call{left:518px;top:62px}
.contact-addr{left:700px;top:64px;text-transform:uppercase}

.nav{left:8px;top:112px;width:872px;height:41px;transform:skewX(-18deg);background:var(--blue);border-left:11px solid var(--navy);border-right:11px solid var(--navy)}
.nav ul{list-style:none;transform:skewX(18deg);height:100%;position:relative}
.nav li{position:absolute;color:#fff;font-size:13.5px;text-transform:uppercase;top:12px}

.hero{left:4px;top:165px;width:872px;height:376px;overflow:hidden;
  background:
    radial-gradient(ellipse 150px 70px at 560px 230px,rgba(12,16,22,.95) 0%,rgba(12,16,22,.7) 55%,rgba(12,16,22,0) 100%),
    radial-gradient(ellipse 90px 30px at 720px 180px,rgba(30,35,45,.75) 0%,rgba(30,35,45,0) 100%),
    radial-gradient(ellipse 330px 220px at 620px 170px,rgba(214,205,200,.95) 0%,rgba(170,178,192,.75) 40%,rgba(80,104,136,0) 100%),
    radial-gradient(ellipse 260px 140px at 830px 340px,rgba(190,200,214,.8) 0%,rgba(190,200,214,0) 100%),
    linear-gradient(100deg,#061428 0%,#0f2a4d 35%,#2a4a72 60%,#3e6088 100%)}
.hero-box{left:37px;top:59px;width:337px;height:211px;background:rgba(4,12,28,.78);padding:16px 12px 0 13px;color:#fff}
.hero-box h1{font-size:22px;line-height:29px;font-weight:700;letter-spacing:.3px;text-transform:uppercase}
.hero-box h2{font-size:13.5px;font-weight:700;color:var(--cyan);margin-top:10px;text-transform:uppercase}
.hero-box p{font-size:13px;line-height:19.5px;margin-top:17px;text-align:justify;padding-left:3px}
.hero-corner{right:10px;bottom:10px}
.hero-brand{left:716px;top:300px;display:flex;align-items:center;gap:8px}
.hero-brand .sq{width:22px;height:22px;background:var(--cyan)}
.hero-brand span{font-size:19px;font-weight:700;color:#fff;line-height:21px;text-transform:uppercase}

.tab{height:41px;top:574px;width:196px;transform:skewX(-18deg);background:var(--blue);border-left:10px solid var(--navy);border-right:9px solid var(--navy)}
.tab span{display:block;transform:skewX(18deg);color:#fff;font-size:19.5px;font-weight:700;line-height:41px;padding-left:11px;text-transform:uppercase;white-space:nowrap}

.card{top:630px;width:182px;height:256px;background:var(--card);padding:7px 8px}
.card-photo{height:111px;width:100%}
.card p{font-size:11px;line-height:16px;margin-top:8px;text-align:justify;color:var(--text)}
.card .more{display:block;margin-top:8px;font-size:11.5px;font-weight:700;color:var(--navy)}

.news-title{left:22px;top:938px;font-size:24px;line-height:28px;font-weight:700;color:var(--navy);text-transform:uppercase}
.news{top:973px;width:412px;height:136px;background:var(--card)}
.news-mark{left:20px;top:17px;width:102px;height:102px;border-radius:50%;background:#d9d9d9;display:flex;align-items:center;justify-content:center;font-size:22px;font-weight:700;color:#2b2b2b}
.news-body{left:142px;top:11px;width:260px}
.news-body h3{font-size:17px;line-height:21px;font-weight:700;color:var(--blue);text-transform:uppercase;letter-spacing:.4px}
.news-body h4{font-size:17px;line-height:21px;font-weight:400;color:var(--muted);text-transform:uppercase}
.news-body p{font-size:13px;line-height:16px;margin-top:4px;color:#333}
.date{margin-top:12px;display:flex;height:22px}
.date span{background:var(--blue);color:#fff;font-size:13px;line-height:22px;padding:0 9px}
.date i{width:28px;background:var(--navy);display:flex;align-items:center;justify-content:center}

.footer{left:0;top:1138px;width:883px;height:48px;background:var(--footer)}
.footer p{position:absolute;left:11px;top:17px;font-size:13px;color:#b5b5b5;text-transform:uppercase}
.social{position:absolute;top:10px;width:29px;height:29px;background:var(--icon);display:flex;align-items:center;justify-content:center;font-size:8.5px;color:#2b2b2b;text-decoration:none}
</style>
</head>
<body>
<div class="page">

  <div class="brand abs">
    <div class="brand-square"></div>
    <div class="brand-name">Halvern Keyworks LLC</div>
  </div>

  <div class="contact contact-call abs">
    <svg width="40" height="42" viewBox="0 0 40 42" aria-hidden="true">
      <rect x="2" y="6" width="18" height="32" rx="3" fill="#111"/>
      <rect x="5" y="11" width="12" height="21" fill="#fff"/>
      <circle cx="26" cy="12" r="12" fill="#111"/>
      <text x="26" y="15.5" font-size="9" fill="#fff" text-anchor="middle" font-family="Roboto Condensed, sans-serif">CALL</text>
    </svg>
    <div>Call Us :<br>TEL: 888-555-0142</div>
  </div>

  <div class="contact contact-addr abs">
    <svg width="30" height="42" viewBox="0 0 30 42" aria-hidden="true">
      <path d="M15 1C7 1 1 7 1 15c0 10 14 26 14 26s14-16 14-26C29 7 23 1 15 1z" fill="#111"/>
      <circle cx="15" cy="14" r="5.5" fill="#fff"/>
    </svg>
    <div>4120 Larkspur Ave<br>Dallas, TX 75299</div>
  </div>

  <nav class="nav abs">
    <ul>
      <li style="left:27px">Home</li>
      <li style="left:114px">About Us</li>
      <li style="left:223px">Services</li>
      <li style="left:331px">Locksmith Services</li>
      <li style="left:506px">Price List</li>
      <li style="left:620px">Contacts</li>
    </ul>
  </nav>

  <section class="hero abs" role="img" aria-label="Photo of a hand holding out a flip car key">
    <div class="hero-box abs">
      <h1>Professional Automotive<br>Locksmith Service.</h1>
      <h2>Special price for used car dealerships!</h2>
      <p>Any model and year of the following makes: Brask, Dunmoral, Marquenne, Carrow, Pell, Tabori, Zephrane, Kelto, Runel, Okarawe, Solumé.</p>
      <svg class="hero-corner abs" width="24" height="24" viewBox="0 0 24 24" aria-hidden="true"><path d="M24 0V24H0z" fill="var(--blue)"/></svg>
    </div>
    <div class="hero-brand abs"><div class="sq"></div><span>Halvern<br>Keyworks</span></div>
  </section>

  <div class="tab abs" style="left:24px"><span>Our Facility</span></div>
  <div class="tab abs" style="left:239px"><span>Service Coverage</span></div>
  <div class="tab abs" style="left:461px"><span>Testimonials</span></div>
  <div class="tab abs" style="left:675px"><span>Service FAQ</span></div>

  <article class="card abs" style="left:24px">
    <div class="card-photo" role="img" aria-label="Photo of a key fob near a car door handle" style="background:linear-gradient(135deg,#1c1f24,#6d727a 55%,#c7c9cc)"></div>
    <p>Lorem Ipsum is simply dummy text of the printing and typesetting industry. Lorem Ipsum has been the industry's standard dummy text ever since the 1500s, when an unknown printer took...</p>
    <span class="more">MORE[+]</span>
  </article>
  <article class="card abs" style="left:240px">
    <div class="card-photo" role="img" aria-label="Photo of a hand holding keys in front of a tall building" style="background:linear-gradient(160deg,#2f7fd6,#8fc0ef 50%,#e6b35a)"></div>
    <p>Lorem Ipsum is simply dummy text of the printing and typesetting industry. Lorem Ipsum has been the industry's standard dummy text ever since the 1500s, when an unknown printer took...</p>
    <span class="more">MORE[+]</span>
  </article>
  <article class="card abs" style="left:458px">
    <div class="card-photo" role="img" aria-label="Photo of satisfied business customers giving thumbs up" style="background:linear-gradient(180deg,#f4f4f4,#b9bcc1 60%,#4a4d52)"></div>
    <p>Lorem Ipsum is simply dummy text of the printing and typesetting industry. Lorem Ipsum has been the industry's standard dummy text ever since the 1500s, when an unknown printer took...</p>
    <span class="more">MORE[+]</span>
  </article>
  <article class="card abs" style="left:672px">
    <div class="card-photo" role="img" aria-label="Photo of support staff wearing headsets" style="background:linear-gradient(180deg,#dfe3e8,#a8a49e 55%,#e9e6e1)"></div>
    <p>Lorem Ipsum is simply dummy text of the printing and typesetting industry. Lorem Ipsum has been the industry's standard dummy text ever since the 1500s, when an unknown printer took...</p>
    <span class="more">MORE[+]</span>
  </article>

  <h2 class="news-title abs">Latest News</h2>

  <article class="news abs" style="left:15px">
    <div class="news-mark abs">QRT</div>
    <div class="news-body abs">
      <h3>Locksmith</h3>
      <h4>News</h4>
      <p>We can now duplicate Kestra, QRT, Ferran and Tarn Ridge keys.</p>
      <div class="date"><span>25 NOV</span><i><svg width="18" height="14" viewBox="0 0 18 14" aria-hidden="true"><path d="M9 1C4.5 1 1 3.6 1 6.6c0 1.6 1 3 2.6 4L2.5 13l3.6-1.6c.9.2 1.9.3 2.9.3 4.5 0 8-2.5 8-5.1S13.5 1 9 1z" fill="none" stroke="#fff" stroke-width="1.4"/></svg></i></div>
    </div>
  </article>

  <article class="news abs" style="left:449px">
    <div class="news-mark abs">TABORI</div>
    <div class="news-body abs">
      <h3>Locksmith</h3>
      <h4>News</h4>
      <p>We will be able to clone Tabori smart keys by the beginning of next month!</p>
      <div class="date"><span>25 NOV</span><i><svg width="18" height="14" viewBox="0 0 18 14" aria-hidden="true"><path d="M9 1C4.5 1 1 3.6 1 6.6c0 1.6 1 3 2.6 4L2.5 13l3.6-1.6c.9.2 1.9.3 2.9.3 4.5 0 8-2.5 8-5.1S13.5 1 9 1z" fill="none" stroke="#fff" stroke-width="1.4"/></svg></i></div>
    </div>
  </article>

  <footer class="footer abs">
    <p>Halvern Keyworks LLC © 2010 | Privacy Policy</p>
    <a class="social" style="left:734px" href="#">Lumo</a>
    <a class="social" style="left:768px" href="#">Chirra</a>
    <a class="social" style="left:804px" href="#">Nexa</a>
    <a class="social" style="left:839px" href="#" aria-label="News feed">
      <svg width="17" height="17" viewBox="0 0 17 17" aria-hidden="true">
        <circle cx="3" cy="14" r="2.2" fill="#2b2b2b"/>
        <path d="M1.5 7.5a8 8 0 0 1 8 8" fill="none" stroke="#2b2b2b" stroke-width="2.2"/>
        <path d="M1.5 2a13.5 13.5 0 0 1 13.5 13.5" fill="none" stroke="#2b2b2b" stroke-width="2.2"/>
      </svg>
    </a>
  </footer>

</div>
</body>
</html>
```